Verantis Guest Event Collateral

Create a double-sided, oversized piece of collateral for a series of guest networking events that we'll be hosting in 2019

We are looking for this piece of collateral to be the size of an oversized post card (1/2 of an 8/5 x 11 piece of paper). The front should include the following: Verantis's Mission Statement: Continually foster a culture of community and education for focused business professionals. How do we do it? Using four distinct principles, Verantis offers business professionals the opportunity to be successful right now ,as well as next year. Through in-person meetings, virtual meetings, networking events, and educational opportunities Verantis offers members a chance to hit their goals not only this year, but every year! Collaboration: Work with like-minded, driven Verantis members to collaborate and overcome the objections, hurdles and challenges that all business professionals face, either in person at twice monthly meetings, or virtually, from the comfort of your home or office. Accountability: Stay on track, and complete the goals you have set for yourself! Weekly in person or virtual meetings afford all members the opportunity to review their plan twice a month with fellow Verantis members, and trained Verantis coaches. Referrals: In the midst of crafting an executable, measurable and attainable plan let Verantis build your business through a steady stream of referrals via six yearly networking events, specifically designed to ensure you walk away with new referral partners. Strategy: Let Verantis assist you in crafting a strategy within our proven business planning template; realistic, understandable, measurable, beyond normal, attainable and time bound. The back should include the following: Become a Verantis member for $150/month and join us for 6 Networking Events in 2019 plus much more! We aren’t just about collaboration, accountability and strategy! Creating opportunities for referrals is also a cornerstone of Verantis! To make certain we are delivering on this principle, Verantis will host 6 events throughout 2019, complete with specific activities at each event to ensure you meet everyone in the room, making immediate connects to build your referral network. Join now and put yourself in position for success in 2019! Name: Phone: Email: Company Name: Industry: Position: Credit Card Number: Exp. Date: Testimonials: Overall I think people are lazy. I know I am! The benefits I have found and have come to truly appreciate thru Verantis are a sense of professionalism, accountability and shared enthusiasm. These things break that cycle of laziness for me and, I am sure, many others. When I walk into a meeting I know that positive and helpful feedback is the name of the game. Feedback from others and in many other industries from my own has become a key and cornerstone to my business and personal success. I would urge anyone no matter what your occupation to attend a couple of meetings and see how this group of like minded professionals can help you to achieve more. More time, More success, More health, More security, More money, More happiness..............What could you use more of? Gordon T. Melby Sr. Automotive Consultant Ridgewater Leasing & Sales Thank you!

Target Market(s)

Small business owners, entrpreneurs, networkers, sales people

Industry/Entity Type

Business Consultant

Font styles to use
Sans Serif

Colors
f36f22
f68d4e
f8ba93
f78f20
faa54b

Requirements
Must have
• - Imagery
• - Our company logo
• - Clear CTA to check out our website (www.verantis-example.com)
• - Option to "Join the Verantis Community Today!" and include a spot for someone to fill in their name, email address, company name, and phone number
• - Reference that we host 6+ networking events in Denver throughout the year that are free to attend and are unlike any other networking event they've attended before
• - Mention that we have in-person meetings 2x per month, virtual meeting options, networking events, and educational events
• - Highlight the following acronym which references our core company components:
• Collaboration:
• Work with like-minded, driven Verantis members to collaborate and overcome the objections, hurdles and challenges that all business professionals face, in either in person twice monthly meetings, or virtually, from the comfort of your home of office.
• Accountability:
• Stay on track, and complete the goals you have set for yourself! Weekly in person or virtual meetings afford all members the opportunity to review their plan twice a month with your fellow Verantis members and trained Verantis coaches, to make certain you success is continuous throughout the year.
• Referrals:
• In the midst of crafting an executable, measurable and attainable plan let Verantis build your business through a steady stream of referral opportunities via twelve yearly networking events, specifically designed to ensure you walk away with new referral partners.
• Strategy:
• Let Verantis assist you in crafting a strategy within our proven business planning template; realistic, understandable, measurable, beyond normal, attainable and time bound.

```html
<!DOCTYPE html>
<html lang="en">
<head>
<meta charset="utf-8">
<title>Verantis Guest Event Collateral</title>
<link href="https://fonts.googleapis.com/css2?family=Montserrat:wght@300;400;500;600;700&display=swap" rel="stylesheet">
<style>
:root{
  --orange:#f36f22;
  --orange-mid:#f78f20;
  --orange-soft:#f68d4e;
  --orange-pale:#f8ba93;
  --orange-light:#faa54b;
  --ink:#3a3a3a;
  --body:#555;
  --stage:#d9d9d9;
  --panel:#f3f3f3;
  --black:#161616;
}
*{margin:0;padding:0;box-sizing:border-box}
html,body{width:1200px;height:793px;overflow:hidden}
body{background:radial-gradient(ellipse at center,#efefef 0%,var(--stage) 100%);font-family:'Montserrat',sans-serif;position:relative;color:var(--body)}
.sheet{position:absolute;background:#fff;box-shadow:0 4px 14px rgba(0,0,0,.25);overflow:hidden}
.sheet--front{left:62px;top:44px;width:528px;height:684px}
.sheet--back{left:616px;top:42px;width:531px;height:688px}
.page-label{position:absolute;top:742px;font-weight:600;font-size:21px;color:#222;width:300px;text-align:center}
.page-label--front{left:176px}
.page-label--back{left:731px}

/* front */
.hero{position:absolute;left:0;top:0;width:528px;height:380px}
.hero-photo{position:absolute;inset:0;background:linear-gradient(160deg,#8a5a3a 0%,#6d4a35 35%,#c9c2b8 60%,#e8e6e2 100%)}
.hero-chevron{position:absolute;left:0;top:0}
.brand-mark{position:absolute;left:200px;top:130px;display:flex;align-items:center;gap:8px;font-weight:500;font-size:22px;color:#fff;letter-spacing:.5px}
.brand-mark .square{width:16px;height:16px;background:var(--orange-mid)}
.intro{position:absolute;left:24px;top:396px;width:232px}
.intro h1{font-weight:500;font-size:14.5px;line-height:18px;color:var(--ink);letter-spacing:.2px}
.rule{width:98px;height:2px;background:var(--orange-mid);margin:10px 0 13px}
.intro p{font-size:9.3px;line-height:11.6px;color:var(--body);font-weight:400}
.intro p b{color:#333;font-weight:600}
.points{list-style:none;margin-top:15px}
.points li{position:relative;font-size:8.4px;line-height:10.5px;color:#333;font-weight:500;margin-bottom:10px;text-indent:14px}
.points li::before{content:"";position:absolute;left:0;top:1px;width:9px;height:9px;border-radius:50%;background:var(--orange)}
.points li::after{content:"";position:absolute;left:2.5px;top:3px;width:3px;height:4px;border:solid #fff;border-width:0 1.2px 1.2px 0;transform:rotate(40deg)}
.join{position:absolute;left:290px;top:392px;width:207px;height:174px;background:#fff;border-top:2px solid var(--orange-mid);box-shadow:0 1px 6px rgba(0,0,0,.12);padding:12px 13px}
.join h2{text-align:center;font-weight:700;font-size:11.6px;line-height:14.5px;color:var(--orange)}
.field{height:26px;background:var(--panel);margin-top:4px;font-size:8px;color:#777;padding:0 9px;line-height:26px}
.field:first-of-type{margin-top:8px}
.cta{position:absolute;left:291px;top:580px;width:206px;height:26px;background:var(--orange);color:#fff;font-weight:500;font-size:14px;text-align:center;line-height:26px}

/* footer shared */
.footer{position:absolute;left:0;width:100%;height:36px;background:linear-gradient(90deg,var(--orange) 0%,var(--orange-mid) 100%)}
.footer-base{position:absolute;left:0;width:100%;height:14px;background:var(--black)}
.footer .hint{position:absolute;left:54px;top:5px;font-size:5.8px;color:#fff}
.footer .phone{position:absolute;left:52px;top:12px;font-weight:700;font-size:19px;line-height:22px;color:#fff;letter-spacing:.2px}
.footer .phone-icon{position:absolute;left:20px;top:7px}
.footer .contact{position:absolute;top:22px;font-size:7.2px;color:#fff;font-weight:500}
.footer .badge{position:absolute;top:-12px;width:24px;height:24px;border-radius:50%;background:var(--orange);box-shadow:0 0 0 2px #fff}
.footer .badge svg{display:block;margin:6px auto}

/* back */
.masthead{position:absolute;left:21px;top:22px;width:486px;height:68px;background:linear-gradient(180deg,#ededed,#dcdcdc);display:flex;align-items:center;justify-content:center}
.masthead .brand-mark{position:static;color:#444;font-size:30px;font-weight:400;gap:10px}
.masthead .brand-mark .square{width:20px;height:20px}
.feature-photo{position:absolute;left:21px;top:99px;width:486px;height:267px;background:linear-gradient(135deg,#b9a58d 0%,#e7e3dc 45%,#cfc9c0 70%,#9d8a74 100%)}
.approach{position:absolute;left:0;top:384px;width:100%;text-align:center;font-weight:500;font-size:14.4px;color:var(--ink);letter-spacing:.3px}
.approach-rule{position:absolute;left:217px;top:408px;width:97px;height:2px;background:var(--orange-mid)}
.divider{position:absolute;left:266px;top:420px;width:1px;height:214px;background:#e6e6e6}
.pillar{position:absolute;width:224px;text-align:center}
.pillar svg{display:block;margin:0 auto}
.pillar h3{font-weight:500;font-size:13.4px;color:#222;margin:3px 0 4px}
.pillar p{font-size:7.3px;line-height:9.3px;color:#666}
.p1{left:30px;top:414px}.p2{left:282px;top:414px}.p3{left:30px;top:526px}.p4{left:282px;top:526px}
</style>
</head>
<body>

<section class="sheet sheet--front">
  <div class="hero">
    <div class="hero-photo" role="img" aria-label="Photo of a presenter at a whiteboard with seated colleagues in an office with a timber wall"></div>
    <svg class="hero-chevron" width="528" height="380" viewBox="0 0 528 380">
      <polygon points="0,292 264,372 528,292 528,380 0,380" fill="#fff"/>
      <polygon points="0,298 264,372 528,298 528,308 264,384 0,308" fill="var(--orange-mid)"/>
      <polygon points="0,284 264,362 528,284 528,292 264,372 0,292" fill="#4a4a4a"/>
    </svg>
    <div class="brand-mark"><span class="square"></span>VERANTIS</div>
  </div>

  <div class="intro">
    <h1>LEARN SIMPLE STRATEGIES<br>TO ENSURE YOUR SUCCESS</h1>
    <div class="rule"></div>
    <p>Verantis helps you create a plan that you can execute easily and experience success year after year. <b>But we don't stop there.</b> Join the Verantis community and give yourself access to the resources, relationships, and tools that you need to take your career to the next level.</p>
    <ul class="points">
      <li>Reference that we host 6+ networking events in Denver throughout the year that are free to attend and are unlike any other networking event they've attended before.</li>
      <li>Mention that we have in-person meetings 2x per month, virtual meeting options, networking events, and educational events</li>
    </ul>
  </div>

  <div class="join">
    <h2>Join the<br>Verantis Community Today!</h2>
    <div class="field">Name</div>
    <div class="field">E-mail</div>
    <div class="field">Company Name</div>
    <div class="field">Phone Number</div>
  </div>
  <div class="cta">Check out our website</div>

  <div class="footer" style="top:634px">
    <svg class="phone-icon" width="22" height="22" viewBox="0 0 22 22"><circle cx="11" cy="11" r="11" fill="var(--black)"/><rect x="7.5" y="5" width="7" height="12" rx="1.2" fill="none" stroke="#fff" stroke-width="1.4"/><circle cx="11" cy="15" r=".8" fill="#fff"/></svg>
    <span class="hint">Contact us to and out how we can help you.</span>
    <span class="phone">0400 555 0199</span>
    <span class="badge" style="left:338px"><svg width="12" height="12" viewBox="0 0 12 12"><circle cx="6" cy="6" r="6" fill="#fff"/><rect x="2.5" y="3.8" width="7" height="4.8" fill="var(--orange)"/><polyline points="2.5,3.8 6,6.6 9.5,3.8" fill="none" stroke="#fff" stroke-width=".8"/></svg></span>
    <span class="contact" style="left:300px">info@verantis-example.com</span>
    <span class="badge" style="left:460px"><svg width="12" height="12" viewBox="0 0 12 12"><circle cx="6" cy="6" r="5.3" fill="none" stroke="#fff" stroke-width="1"/><ellipse cx="6" cy="6" rx="2.3" ry="5.3" fill="none" stroke="#fff" stroke-width=".8"/><line x1=".7" y1="6" x2="11.3" y2="6" stroke="#fff" stroke-width=".8"/></svg></span>
    <span class="contact" style="left:420px">www.verantis-example.com</span>
  </div>
  <div class="footer-base" style="top:670px"></div>
</section>

<section class="sheet sheet--back">
  <div class="masthead"><div class="brand-mark"><span class="square"></span>VERANTIS</div></div>
  <div class="feature-photo" role="img" aria-label="Photo of hands reviewing printed charts and reports on a wooden desk"></div>

  <h2 class="approach">VERANTIS OFFERS A FOUR-PRONGED APPROACH:</h2>
  <div class="approach-rule"></div>
  <div class="divider"></div>

  <div class="pillar p1">
    <svg width="34" height="26" viewBox="0 0 34 26"><circle cx="14" cy="7" r="6" fill="var(--orange-soft)"/><path d="M3 26v-4a8 8 0 0 1 8-8h6a8 8 0 0 1 8 8v4z" fill="var(--orange-soft)"/><path d="M26 12l6 6M32 12l-6 6" stroke="var(--orange)" stroke-width="2"/></svg>
    <h3>Collaboration</h3>
    <p>Work with like-minded, driven Verantis members to collaborate and overcome the objections, hurdles and challenges that all business professionals face, in either in person twice monthly meetings, or virtually, from the comfort of your home of office.</p>
  </div>
  <div class="pillar p2">
    <svg width="28" height="26" viewBox="0 0 28 26"><g stroke="var(--orange)" stroke-width="2" fill="none"><polyline points="1,3 3,5 7,1"/><polyline points="1,12 3,14 7,10"/><polyline points="1,21 3,23 7,19"/></g><g fill="var(--orange-soft)"><rect x="10" y="2" width="17" height="3"/><rect x="10" y="11" width="17" height="3"/><rect x="10" y="20" width="17" height="3"/></g></svg>
    <h3>Accountability</h3>
    <p>Stay on track, and complete the goals you have set for yourself! Weekly in person or virtual meetings afford all members the opportunity to review their plan twice a month with your fellow Verantis members and trained Verantis coaches, to make certain you success is continuous throughout the year.</p>
  </div>
  <div class="pillar p3">
    <svg width="30" height="24" viewBox="0 0 30 24"><g fill="var(--orange-soft)"><rect x="1" y="18" width="4" height="6"/><rect x="7" y="14" width="4" height="10"/><rect x="13" y="10" width="4" height="14"/><rect x="19" y="6" width="4" height="18"/></g><rect x="25" y="0" width="4" height="24" fill="var(--orange)"/></svg>
    <h3>Referrals</h3>
    <p>In the midst of crafting an executable, measurable and attainable plan let Verantis build your business through a steady stream of referral opportunities via twelve yearly networking events, specifically designed to ensure you walk away with new referral partners.</p>
  </div>
  <div class="pillar p4">
    <svg width="30" height="24" viewBox="0 0 30 24"><polygon points="15,2 29,9 15,16 1,9" fill="var(--orange)"/><path d="M7 12v6c4 4 12 4 16 0v-6l-8 4z" fill="var(--orange-soft)"/><line x1="27" y1="10" x2="27" y2="19" stroke="var(--orange)" stroke-width="1.5"/></svg>
    <h3>Strategy</h3>
    <p>Let Verantis assist you in crafting a strategy within our proven business planning template; realistic, understandable, measurable, beyond normal, attainable and time bound.</p>
  </div>

  <div class="footer" style="top:638px">
    <svg class="phone-icon" width="22" height="22" viewBox="0 0 22 22"><circle cx="11" cy="11" r="11" fill="var(--black)"/><rect x="7.5" y="5" width="7" height="12" rx="1.2" fill="none" stroke="#fff" stroke-width="1.4"/><circle cx="11" cy="15" r=".8" fill="#fff"/></svg>
    <span class="hint">Contact us to and out how we can help you.</span>
    <span class="phone">0400 555 0199</span>
    <span class="badge" style="left:339px"><svg width="12" height="12" viewBox="0 0 12 12"><circle cx="6" cy="6" r="6" fill="#fff"/><rect x="2.5" y="3.8" width="7" height="4.8" fill="var(--orange)"/><polyline points="2.5,3.8 6,6.6 9.5,3.8" fill="none" stroke="#fff" stroke-width=".8"/></svg></span>
    <span class="contact" style="left:301px">info@verantis-example.com</span>
    <span class="badge" style="left:461px"><svg width="12" height="12" viewBox="0 0 12 12"><circle cx="6" cy="6" r="5.3" fill="none" stroke="#fff" stroke-width="1"/><ellipse cx="6" cy="6" rx="2.3" ry="5.3" fill="none" stroke="#fff" stroke-width=".8"/><line x1=".7" y1="6" x2="11.3" y2="6" stroke="#fff" stroke-width=".8"/></svg></span>
    <span class="contact" style="left:421px">www.verantis-example.com</span>
  </div>
  <div class="footer-base" style="top:674px"></div>
</section>

<div class="page-label page-label--front">Front Page</div>
<div class="page-label page-label--back">Back Page</div>

</body>
</html>
```